Fotógrafo necesita portada completa para un libro de negocios enfocado a fotografía

Necesito la portada, contraportada y lomo de un libro de tapa blanda que venderé en Librovia llamado “Las claves para prosperar con la cámara”. Adjunto medidas requeridas por Librovia.

“Las claves para prosperar con la cámara” es un libro de negocios orientado a fotógrafos, no un libro de fotografía en sí mismo. Detallo las necesidades a continuación:

- Descripción general: Necesito que el diseño sea llamativo, pero lo suficientemente sencillo, moderno y atractivo como para que el cliente perciba en el diseño que el interior contiene un gran valor. No quiero elementos recargados ni diseños muy complicados de entender. Para más inspiración, ver las portadas de libros como "Las mañas del pudiente", "La mente del capital", "rutinas mínimas", siguiendo el estilo de mi marca personal: www.rodrigovelmar.com
- Portada: La portada debe expresar sensaciones de emoción y libertad (al emprender un negocio fotográfico de la forma que transmito en el interior del libro), pero también de misterio (debido a esos “secretos” para vivir del negocio de la fotografía)
- Contraportada: dividida en dos secciones: Una para la breve descripción del libro y otra para la descripción de la biografía del autor con foto.

Por último, necesito el diseño editable en .PSD con los textos provisionales “lorem ipsum”, ya que todavía no tengo los textos definitivos y seré yo quien los integre, así que aprovecharé esos campos de texto, con la fuente, tamaño y color para hacerlo.

Target Market(s)

Photographers

Industry/Entity Type

Photography, economy, marketing

Font styles to use
Serif
Sans Serif

Requirements
Must have
• Title: Las claves para prosperar con la cámara (Capital or not. Depending on design), Subtitle: El manual completo para trabajar con tu cámara sin perder la cabeza en el camino. Author: Rodrigo Velmar
Should not have
• pictures, photos, ¿gradients?

```html
<!DOCTYPE html>
<html lang="es">
<head>
<meta charset="utf-8">
<title>Las claves para prosperar con la cámara — cubierta completa</title>
<link rel="stylesheet" href="https://fonts.googleapis.com/css2?family=Playfair+Display:wght@700;800&family=Encode+Sans+Condensed:wght@300;400&family=Montserrat:wght@400;500&display=swap">
<style>
  :root {
    --stage: #d8d8d8;
    --sand: #a99783;
    --navy: #1b2240;
    --navy-back: #26304f;
    --emblem-red: #9d1a1c;
    --gold: #c8b397;
    --paper: #dedede;
  }
  * { margin: 0; padding: 0; box-sizing: border-box; }
  html, body { width: 1200px; height: 778px; overflow: hidden; }
  body { background: var(--stage); position: relative; font-family: "Encode Sans Condensed", sans-serif; }

  .cover-wrap { position: absolute; left: 142px; top: 59px; width: 916px; height: 660px; display: flex; box-shadow: 0 10px 30px rgba(0,0,0,.25); }

  /* Back cover */
  .back-cover { position: relative; width: 438px; height: 660px; background: var(--navy-back); color: var(--gold); }
  .back-mark { position: absolute; left: 194px; top: 38px; width: 50px; height: 50px; border-radius: 50%; background: var(--gold); }
  .back-title { position: absolute; left: 0; right: 0; top: 98px; text-align: center; font-family: "Playfair Display", serif; font-weight: 700; font-size: 25px; line-height: 28px; letter-spacing: -0.5px; }
  .back-subtitle { position: absolute; left: 40px; right: 40px; top: 238px; text-align: center; font-size: 15px; line-height: 19px; font-weight: 300; }
  .blurb { position: absolute; left: 40px; right: 40px; top: 292px; font-size: 8.6px; line-height: 13px; text-align: justify; font-weight: 300; }
  .author-photo { position: absolute; left: 40px; top: 400px; width: 62px; height: 110px; background: var(--paper); }
  .author-bio { position: absolute; left: 116px; right: 40px; top: 402px; font-size: 8.6px; line-height: 13.6px; text-align: justify; font-weight: 300; }
  .isbn-box { position: absolute; right: 40px; top: 555px; width: 88px; height: 88px; background: var(--paper); }

  /* Spine */
  .spine { position: relative; width: 40px; height: 660px; background: var(--navy); color: var(--gold); }
  .spine-mark { position: absolute; left: 11px; top: 16px; width: 18px; height: 18px; border-radius: 50%; background: var(--gold); }
  .spine-text { position: absolute; left: 40px; top: 46px; width: 600px; height: 40px; transform-origin: 0 0; transform: rotate(90deg); display: flex; align-items: center; justify-content: space-between; padding-right: 24px; }
  .spine-titles { display: flex; flex-direction: column; justify-content: center; }
  .spine-title { font-family: "Playfair Display", serif; font-weight: 700; font-size: 12px; letter-spacing: 1.5px; line-height: 14px; }
  .spine-subtitle { font-family: "Montserrat", sans-serif; font-size: 5.6px; letter-spacing: 0.8px; }
  .spine-author { font-family: "Playfair Display", serif; font-weight: 700; font-size: 16px; letter-spacing: 2px; }

  /* Front cover */
  .front-cover { position: relative; width: 438px; height: 660px; background: var(--navy); overflow: hidden; }
  .front-top { position: absolute; left: 0; top: 0; width: 438px; height: 373px; background: var(--sand); }
  .front-title { position: absolute; right: 26px; top: 22px; text-align: right; font-family: "Playfair Display", serif; font-weight: 800; color: var(--navy); font-size: 50px; line-height: 56px; letter-spacing: -1px; }
  .front-emblem { position: absolute; left: 101px; top: 296px; width: 234px; height: 234px; }
  .front-author { position: absolute; left: 0; right: 0; top: 578px; text-align: center; font-family: "Playfair Display", serif; font-weight: 800; font-size: 30px; color: var(--gold); }
</style>
</head>
<body>
<main class="cover-wrap">
  <section class="back-cover">
    <div class="back-mark" role="img" aria-label="Ilustración pequeña del diafragma de una cámara"></div>
    <h2 class="back-title">Las claves<br>para prosperar<br>con la<br>cámara</h2>
    <p class="back-subtitle">El manual completo para trabajar con tu cámara sin perder la cabeza en el camino</p>
    <p class="blurb">“Lorem ipsum dolor sit amet, consectetur adipiscing elit, sed do eiusmod tempor incididunt ut labore et dolore magna aliqua. Ut enim ad minim veniam, quis nostrud exercitation ullamco laboris nisi ut aliquip ex ea commodo consequat. Duis aute irure dolor in reprehenderit in voluptate velit esse cillum dolore eu fugiat nulla pariatur. Excepteur sint occaecat cupidatat non proident, sunt in culpa qui officia deserunt mollit anim id est laborum.”</p>
    <div class="author-photo" role="img" aria-label="Foto del autor"></div>
    <p class="author-bio">“Lorem ipsum dolor sit amet, consectetur adipiscing elit, sed do eiusmod tempor incididunt ut labore et dolore magna aliqua. Ut enim ad minim veniam, quis nostrud exercitation ullamco laboris nisi ut aliquip ex ea commodo consequat. Duis aute irure dolor in reprehenderit in voluptate velit esse cillum dolore eu fugiat nulla pariatur. Excepteur sint occaecat cupidatat non proident, sunt in culpa qui officia deserunt mollit anim id est laborum.”</p>
    <div class="isbn-box"></div>
  </section>

  <section class="spine">
    <div class="spine-mark" role="img" aria-label="Ilustración mínima del diafragma de una cámara"></div>
    <div class="spine-text">
      <div class="spine-titles">
        <span class="spine-title">Las claves para prosperar con la cámara</span>
        <span class="spine-subtitle">El manual completo para trabajar con tu cámara sin perder la cabeza en el camino</span>
      </div>
      <span class="spine-author">Rodrigo Velmar</span>
    </div>
  </section>

  <section class="front-cover">
    <div class="front-top"></div>
    <h1 class="front-title">Las claves<br>para prosperar<br>con la<br>cámara</h1>
    <svg class="front-emblem" viewBox="-117 -117 234 234">
      <defs>
        <path id="subtitle-ring" d="M -8 97 A 97 97 0 1 1 8 97"/>
      </defs>
      <circle r="117" fill="var(--navy)"/>
      <circle r="77" fill="var(--emblem-red)" role="img" aria-label="Ilustración del diafragma de una cámara en rojo"/>
      <text font-family="Montserrat, sans-serif" font-size="10.4" fill="var(--gold)" letter-spacing="0.4">
        <textPath href="#subtitle-ring" startOffset="1%">El manual completo para trabajar con tu cámara sin perder la cabeza en el camino</textPath>
      </text>
      <circle cx="0" cy="100" r="2.6" fill="var(--gold)"/>
    </svg>
    <p class="front-author">Rodrigo Velmar</p>
  </section>
</main>
</body>
</html>
```